Waste Oil Filter collection & disposal

Basically I need a 1 page website for the business called Brenmoor Waste Solutions.
We are a environmental service provider and we collect and dispose of waste oil filters to protect the environment from hazardous waste oil products.

This is the link to our current website: www.brenmoorwaste.co.nz

we want it to look fresh and better than our current website. we may potentially look at getting a new logo designed and are open to ideas/designs if you have any.

Industry/Entity Type

Business

Logo Text

Brenmoor Waste Solutions

Number of Pages Required

1 page

Requirements
Must have
• same colours as current website.
• description of what service we provide please refer to leaflet attached

```html
<!DOCTYPE html>
<html lang="en">
<head>
<meta charset="utf-8">
<title>Contact Us – Brenmoor Waste Solutions</title>
<link href="https://fonts.googleapis.com/css2?family=Open+Sans:wght@400;600;700&display=swap" rel="stylesheet">
<style>
  :root {
    --paper: #ececec;
    --charcoal: #4b4848;
    --field: #393635;
    --field-edge: #2b2928;
    --ink-light: #ffffff;
    --ink-soft: #e6e6e6;
    --brand-green: #5cb85c;
  }
  * { box-sizing: border-box; margin: 0; padding: 0; }
  html, body { width: 1200px; height: 954px; overflow: hidden; }
  body {
    position: relative;
    background: var(--paper);
    font-family: "Open Sans", Arial, sans-serif;
    color: var(--ink-light);
  }
  .backdrop { position: absolute; inset: 0; width: 1200px; height: 954px; }
  .contact-heading {
    position: absolute; left: 226px; top: 338px;
    font-size: 50px; font-weight: 700; line-height: 1; letter-spacing: 0.5px;
  }
  .contact-tagline {
    position: absolute; left: 216px; top: 400px;
    font-size: 26px; font-weight: 400; line-height: 1;
  }
  .brand {
    position: absolute; left: 667px; top: 326px;
    display: flex; align-items: center; gap: 14px;
  }
  .brand-square { width: 58px; height: 58px; background: var(--brand-green); }
  .brand-name {
    font-size: 19px; font-weight: 600; line-height: 1.12; color: var(--ink-light);
  }
  .contact-line {
    position: absolute; display: flex; align-items: flex-start; gap: 14px;
  }
  .contact-phone { left: 176px; top: 526px; align-items: center; }
  .contact-phone .contact-text { font-size: 26px; font-weight: 400; }
  .contact-address { left: 190px; top: 632px; }
  .contact-address .contact-text { font-size: 18px; font-weight: 600; line-height: 1.4; letter-spacing: -0.3px; }
  .contact-form { position: absolute; left: 0; top: 0; }
  .field {
    position: absolute;
    background: var(--field);
    border: 1px solid var(--field-edge);
    color: var(--ink-soft);
    font-family: "Open Sans", Arial, sans-serif;
    font-size: 19px;
    padding: 2px 10px;
    outline: none;
  }
  .field::placeholder { color: var(--ink-soft); opacity: 1; }
  .field-name { left: 509px; top: 504px; width: 193px; height: 31px; }
  .field-email { left: 756px; top: 504px; width: 193px; height: 31px; }
  .field-phone { left: 509px; top: 569px; width: 193px; height: 31px; }
  .field-subject { left: 756px; top: 569px; width: 193px; height: 31px; }
  .field-message { left: 513px; top: 635px; width: 436px; height: 101px; resize: none; padding-top: 0; }
  .send-button {
    position: absolute; left: 890px; top: 766px;
    background: none; border: none; color: var(--ink-light);
    font-family: "Open Sans", Arial, sans-serif; font-size: 20px; font-weight: 700;
    cursor: pointer;
  }
</style>
</head>
<body>
  <svg class="backdrop" viewBox="0 0 1200 954" aria-hidden="true">
    <polygon points="0,311 948,0 1200,0 1200,954 0,954" fill="var(--charcoal)"/>
  </svg>

  <h1 class="contact-heading">CONTACT US</h1>
  <p class="contact-tagline">We appreciate this very Much</p>

  <div class="brand">
    <span class="brand-square"></span>
    <span class="brand-name">Brenmoor<br>Waste<br>Solutions</span>
  </div>

  <div class="contact-line contact-phone">
    <svg width="42" height="44" viewBox="0 0 42 44" aria-hidden="true">
      <path d="M10 2 L16 12 Q17 14 15 16 L12 19 Q16 28 24 33 L27 30 Q29 28 31 29 L40 35 Q42 37 40 39 L36 42 Q32 45 24 41 Q8 32 3 16 Q1 8 5 4 Z" fill="var(--ink-light)"/>
    </svg>
    <span class="contact-text">06 555 0148</span>
  </div>

  <div class="contact-line contact-address">
    <svg width="34" height="46" viewBox="0 0 34 46" aria-hidden="true">
      <path d="M17 2 C8 2 2 9 2 17 C2 28 17 44 17 44 C17 44 32 28 32 17 C32 9 26 2 17 2 Z M17 10 A7 7 0 1 1 16.99 10 Z" fill="var(--ink-light)" fill-rule="evenodd"/>
    </svg>
    <span class="contact-text">Harlow Road, Marston 4820<br>, New Zealand</span>
  </div>

  <form class="contact-form" action="#">
    <input class="field field-name" type="text" placeholder="Name">
    <input class="field field-email" type="email" placeholder="Email">
    <input class="field field-phone" type="tel" placeholder="Phone">
    <input class="field field-subject" type="text" placeholder="Subject">
    <textarea class="field field-message" placeholder="Message"></textarea>
    <button class="send-button" type="submit">Send</button>
  </form>
</body>
</html>
```